We need a banner ad design for a company based in Brazil called "Zunaro" (http://www.zunaro-exemplo.com.br), which offers escort services for men. Our main strength and focus is helping people easily search for escorts using mobile devices, by being an mobile optimized repository of escorts which are crawled from many non-mobile optimized sites.

Target Market(s)

Men at all ages (above 18) looking for escorts

Industry/Entity Type

Escort

Requirements
Must have
• Size must be 468x60
The logo must be on white background
Nice to have
• The banner could have an eye-catching animation

The banner could have a small and quick animation showing the usage of the mobile application (like navigating through the application).
Should not have
• If animated then the text should not be split between frames.

```html
<!DOCTYPE html>
<html lang="pt-BR">
<head>
<meta charset="utf-8">
<title>Zunaro — banners 468x60</title>
<link rel="stylesheet" href="https://fonts.googleapis.com/css2?family=Open+Sans:wght@400;700&display=swap">
<style>
  :root {
    --stage-center: #5a5a5a;
    --stage-edge: #1e1e1e;
    --banner-bg: #ffffff;
    --brand-red: #8c1526;
    --copy-grey: #6f6f6f;
    --device-body: #141414;
    --device-edge: #3a3a3a;
    --screen-white: #ffffff;
  }
  * { margin: 0; padding: 0; box-sizing: border-box; }
  html, body { width: 1200px; height: 900px; overflow: hidden; }
  body {
    background: radial-gradient(ellipse at 50% 45%, var(--stage-center) 0%, #3a3a3a 45%, var(--stage-edge) 100%);
    font-family: "Open Sans", Arial, sans-serif;
    position: relative;
  }
  .banner {
    position: absolute;
    left: 134px;
    width: 932px;
    height: 120px;
    background: var(--banner-bg);
  }
  .banner--1 { top: 32px; }
  .banner--2 { top: 208px; }
  .banner--3 { top: 384px; }
  .banner--4 { top: 560px; }
  .banner--5 { top: 736px; }

  .brand {
    position: absolute;
    left: 18px;
    top: 0;
    height: 120px;
    display: flex;
    align-items: center;
    gap: 10px;
  }
  .brand__dot {
    width: 22px; height: 22px;
    border-radius: 50%;
    background: var(--brand-red);
  }
  .brand__name {
    font-weight: 700;
    font-size: 38px;
    color: var(--brand-red);
    letter-spacing: -0.5px;
  }
  .tagline {
    position: absolute;
    left: 270px;
    top: 14px;
    width: 380px;
    text-align: center;
    font-size: 29px;
    line-height: 31px;
    color: var(--copy-grey);
    font-weight: 400;
  }
  .device {
    position: absolute;
    left: 676px;
    top: 6px;
    width: 226px;
    height: 108px;
    background: var(--device-body);
    border: 2px solid var(--device-edge);
    border-radius: 18px;
  }
  .device__screen {
    position: absolute;
    left: 28px;
    top: 10px;
    width: 162px;
    height: 84px;
    overflow: hidden;
  }
  .device__button {
    position: absolute;
    right: 10px;
    top: 42px;
    width: 20px; height: 20px;
    border-radius: 50%;
    border: 2px solid var(--device-edge);
  }
  .screen--brand {
    background: var(--screen-white);
    display: flex;
    align-items: center;
    justify-content: center;
  }
  .screen--brand .brand__name { font-size: 24px; }
  .screen--photo-1 { background: linear-gradient(135deg, #f4efe6, #e8c9a4 55%, #d8b27a); }
  .screen--photo-2 { background: linear-gradient(160deg, #d9d6cf, #7a6a5c 50%, #4a4038); }
  .screen--photo-3 { background: linear-gradient(170deg, #c8d8e0, #b48672 50%, #6d8aa0); }
  .screen--photo-4 { background: linear-gradient(150deg, #2a2424, #b89a88 55%, #3a3030); }
</style>
</head>
<body>

<section class="banner banner--1">
  <div class="brand"><span class="brand__dot"></span><span class="brand__name">Zunaro</span></div>
  <p class="tagline">O maior catálogo de acompanhantes na palma da sua mão</p>
  <div class="device">
    <div class="device__screen screen--brand"><span class="brand__name">Zunaro</span></div>
    <span class="device__button"></span>
  </div>
</section>

<section class="banner banner--2">
  <div class="brand"><span class="brand__dot"></span><span class="brand__name">Zunaro</span></div>
  <p class="tagline">O maior catálogo de acompanhantes na palma da sua mão</p>
  <div class="device">
    <div class="device__screen screen--photo-1" role="img" aria-label="Foto de perfil de uma acompanhante loira"></div>
    <span class="device__button"></span>
  </div>
</section>

<section class="banner banner--3">
  <div class="brand"><span class="brand__dot"></span><span class="brand__name">Zunaro</span></div>
  <p class="tagline">O maior catálogo de acompanhantes na palma da sua mão</p>
  <div class="device">
    <div class="device__screen screen--photo-2" role="img" aria-label="Foto de uma acompanhante deitada"></div>
    <span class="device__button"></span>
  </div>
</section>

<section class="banner banner--4">
  <div class="brand"><span class="brand__dot"></span><span class="brand__name">Zunaro</span></div>
  <p class="tagline">O maior catálogo de acompanhantes na palma da sua mão</p>
  <div class="device">
    <div class="device__screen screen--photo-3" role="img" aria-label="Foto de uma acompanhante recostada em almofadas"></div>
    <span class="device__button"></span>
  </div>
</section>

<section class="banner banner--5">
  <div class="brand"><span class="brand__dot"></span><span class="brand__name">Zunaro</span></div>
  <p class="tagline">O maior catálogo de acompanhantes na palma da sua mão</p>
  <div class="device">
    <div class="device__screen screen--photo-4" role="img" aria-label="Foto de uma acompanhante morena em tons escuros"></div>
    <span class="device__button"></span>
  </div>
</section>

</body>
</html>
```